Label and logo design for organic food range

We are looking to a new label and logo design for a brand new range of organic foods. We have a conventional product range branded as dalvenhof and we are launching a new line of organic products under the brandname "ecomerla"

For reference I attached the logo of dalvenhof which we like it very much, but we think that we would need an upgraded, more fresh logo design for our new brand.

I also attached a label for a dalvenhof product, we use only one label on the products (packed in transparent bags), so the label must contains a lot of text and informations as you can see on the dalvenhof label. (mostly it should contain all the text on the label attached)

Target Market(s)

organic products, bio products, health stores

Industry/Entity Type

Health Product

Logo Text

the healthy choice

Font styles to use
Sans Serif
Other font styles liked:
• CabinSketch, Bebas Neue, Chalkboard,

Colors
9bcb3b
00a990
fbed22
f78f20
faa54b
fac994
f37122
f68d4d
ec1f27

Requirements
Nice to have
• As a reference, I attached 3 labels (same brand I like very much, 1,2,3.jpg). Default label size is 64mm x 100mm ( + 2.5mm bleed). I also attached the texts on the label (label-text.docx)

```html
<!DOCTYPE html>
<html lang="ro">
<head>
<meta charset="utf-8">
<title>ecomerla – identitate și etichetă</title>
<link rel="stylesheet" href="https://fonts.googleapis.com/css2?family=Bebas+Neue&family=Cabin+Sketch:wght@400;700&family=Lato:ital,wght@0,400;0,700;1,400&display=swap">
<style>
  :root {
    --teal: #00a990;
    --white: #ffffff;
    --yellow: #fbed22;
    --ink: #1f3d36;
    --paper: #ffffff;
  }
  * { box-sizing: border-box; margin: 0; padding: 0; }
  html, body { width: 848px; height: 1200px; overflow: hidden; background: var(--paper); }
  .board { position: relative; width: 848px; height: 1200px; font-family: "Lato", sans-serif; }

  .brand-name {
    font-family: "Bebas Neue", sans-serif;
    letter-spacing: 6px;
    line-height: 1;
  }
  .brand-tag {
    font-family: "Bebas Neue", sans-serif;
    letter-spacing: 4px;
    line-height: 1;
  }

  .logo-light {
    position: absolute; left: 96px; top: 140px; width: 300px;
    text-align: center; color: var(--teal);
  }
  .logo-light .brand-name { font-size: 54px; }
  .logo-light .brand-tag { font-size: 14px; margin-top: 22px; }

  .logo-dark {
    position: absolute; left: 514px; top: 67px; width: 334px; height: 240px;
    background: var(--teal); color: var(--white);
    display: flex; flex-direction: column; align-items: center; justify-content: center;
  }
  .logo-dark .brand-name { font-size: 42px; }
  .logo-dark .brand-tag { font-size: 11px; margin-top: 18px; }

  .label {
    position: absolute; left: 258px; top: 622px; width: 336px; height: 454px;
    background: var(--teal); color: var(--white);
    text-align: center; overflow: hidden;
  }
  .label .brand-name { font-size: 36px; margin-top: 72px; }
  .label .brand-tag { font-size: 10px; margin-top: 16px; }
  .product-name {
    font-family: "Cabin Sketch", sans-serif; font-weight: 700;
    color: var(--yellow); font-size: 25px; letter-spacing: 1px;
    margin-top: 36px;
  }
  .product-rule { width: 42px; height: 2px; background: var(--yellow); margin: 10px auto 0; }
  .label-copy {
    font-size: 8.3px; line-height: 1.35; padding: 0 30px; margin-top: 20px;
  }
  .label-copy b { font-weight: 700; }
  .label-note { font-size: 8.3px; line-height: 1.35; padding: 0 36px; margin-top: 10px; }
  .note-icon {
    display: inline-block; width: 7px; height: 7px; border-radius: 50%;
    background: var(--white); vertical-align: 0; margin-right: 3px;
  }
  .nutrition { margin: 24px 40px 0; }
  .nutrition-title {
    display: flex; align-items: center; gap: 6px;
    font-family: "Bebas Neue", sans-serif; font-size: 8px; letter-spacing: .3px;
  }
  .nutrition-title::before, .nutrition-title::after { content: ""; flex: 1; height: 1px; background: var(--white); }
  .nutrition-row {
    display: grid; grid-template-columns: 1.45fr 1fr .7fr; text-align: left;
    font-size: 6px; margin-top: 8px;
  }
  .nutrition-row span b { font-family: "Bebas Neue", sans-serif; font-size: 7.5px; font-weight: 400; margin-right: 8px; letter-spacing: .2px; }
  .nutrition-rule { height: 1px; background: var(--white); margin-top: 14px; }
  .distributor { font-size: 8.3px; line-height: 1.35; margin-top: 10px; }
  .packed-badge {
    position: absolute; left: 50%; bottom: -2px; transform: translateX(-50%);
    width: 126px; height: 20px; border-radius: 12px 12px 0 0;
    background: var(--yellow); color: var(--ink);
    font-size: 6.5px; font-style: italic; line-height: 20px;
  }
</style>
</head>
<body>
<main class="board">
  <div class="logo-light">
    <div class="brand-name">ECOMERLA</div>
    <div class="brand-tag">ORGANIC FOOD</div>
  </div>

  <div class="logo-dark">
    <div class="brand-name">ECOMERLA</div>
    <div class="brand-tag">ORGANIC FOOD</div>
  </div>

  <section class="label">
    <div class="brand-name">ECOMERLA</div>
    <div class="brand-tag">ORGANIC FOOD</div>
    <h1 class="product-name">GRANOLA</h1>
    <div class="product-rule"></div>
    <p class="label-copy">
      <b>Mod de utilizare:</b> Se pot consuma ca atare sau prăjite în diverse combinații cu legume, sosuri, cereale și deserturi. A se consuma, de preferință, înainte de data marcată pe ambalaj.
      <b>Ingrediente:</b> sâmburi de Migdale crude. <b>Depozitare:</b> A se păstra la loc uscat și răcoros. <b>Atenționare:</b> produsul conține substanțe cu potențial alergen: migdale. <b>Țara de origine:</b> SUA.
    </p>
    <p class="label-note"><span class="note-icon"></span>Produs într-o unitate care ambalează și procesează făină din cereale, muștar, soia, nuci, alune, semințe de susan.</p>
    <div class="nutrition">
      <div class="nutrition-title">VALORI NUTRITIONALE / 100GR</div>
      <div class="nutrition-row"><span><b>ENERGIE</b>2728kJ / 659 kcal</span><span><b>GRASIMI</b>55.8 g</span><span><b>PROTEIN</b>55.8 g</span></div>
      <div class="nutrition-row"><span><b>ENERGIE</b>2728kJ / 659 kcal</span><span><b>GRASIMI</b>55.8 g</span><span><b>PROTEIN</b>55.8 g</span></div>
      <div class="nutrition-rule"></div>
    </div>
    <p class="distributor"><b>Distribuitor:</b> Norvel Trade SRL<br>Sibiu, str. Fagului 12</p>
    <div class="packed-badge">Ambalat in Romania</div>
  </section>
</main>
</body>
</html>
```